Kestrel Business Accountants , logo & business card design

I am a business consultant & accountant , servicing a range of small business clients , providing business & taxation advice.
I am looking for a logo & business card design that is not traditional accounting style.
Something colorful & innovative would be good.
Target Market(s)
Small businesses in their growth stage
Industry/Entity Type
Business Consultant
Contact Information for Business Card
Kestrel Business Accountants Pty Ltd
Miles Hartley CPA
Director
Ph: 0413 8064 91
Email : kestrel@pallinet.com.au
On reverse of card:
"Kestrel Sight for your Business"
Business Consulting
Taxation
Superannuation
Logo styles of interest
Abstract Logo
Wordmark Logo
Look and feel

```html
<!DOCTYPE html>
<html lang="en">
<head>
<meta charset="utf-8">
<title>Kestrel Business Accountants – Business Card</title>
<link rel="stylesheet" href="https://fonts.googleapis.com/css2?family=Mulish:wght@300;400;700;800&display=swap">
<style>
  :root {
    --page: #ffffff;
    --card-blue: #0d5298;
    --card-blue-soft: #15609f;
    --band-dark: #0b1a3d;
    --ink: #0a0f1e;
    --ink-navy: #0b1f45;
    --white: #ffffff;
    --shadow: rgba(0, 0, 0, 0.35);
  }
  * { margin: 0; padding: 0; box-sizing: border-box; }
  html, body {
    width: 1200px;
    height: 1000px;
    overflow: hidden;
    background: var(--page);
    font-family: "Mulish", "Century Gothic", sans-serif;
  }
  .canvas { position: relative; width: 1200px; height: 1000px; }

  .card {
    position: absolute;
    width: 458px;
    height: 794px;
    background: var(--card-blue);
    box-shadow: 3px 4px 6px var(--shadow);
    overflow: hidden;
  }
  .card--front { left: 143px; top: 48px; }
  .card--back  { left: 642px; top: 164px; }

  .card__texture {
    position: absolute;
    inset: 0;
    background: radial-gradient(ellipse at 50% 45%, var(--card-blue-soft), var(--card-blue) 70%);
  }

  .band {
    position: absolute;
    left: 0;
    width: 100%;
    background: linear-gradient(to bottom, var(--band-dark) 0%, rgba(11, 26, 61, 0.55) 30%, rgba(11, 26, 61, 0) 100%);
  }
  .band--rule { height: 14px; }
  .band--strip { height: 16px; }

  /* Front */
  .brand {
    position: absolute;
    left: 30px;
    top: 30px;
    display: flex;
    align-items: center;
    gap: 10px;
  }
  .brand__square { width: 108px; height: 109px; background: var(--white); flex: none; }
  .brand__name {
    color: var(--white);
    font-weight: 300;
    font-size: 29px;
    line-height: 38px;
    letter-spacing: 0.2px;
  }

  .arrow {
    position: absolute;
    left: 50%;
    transform: translateX(-50%);
    width: 28px;
    height: 18px;
  }
  .arrow--up { top: 291px; }
  .arrow--down { top: 458px; }

  .role {
    position: absolute;
    top: 341px;
    width: 100%;
    text-align: center;
    color: var(--white);
    font-weight: 300;
    font-size: 27px;
  }
  .person {
    position: absolute;
    top: 390px;
    width: 100%;
    text-align: center;
    color: var(--ink);
    font-weight: 800;
    font-size: 28px;
    letter-spacing: 0.3px;
  }
  .contact {
    position: absolute;
    width: 100%;
    text-align: center;
    color: var(--ink-navy);
    font-weight: 300;
    font-size: 26px;
  }
  .contact__label { font-weight: 800; color: var(--ink); }
  .contact--phone { top: 572px; }
  .contact--email { top: 653px; }

  /* Back */
  .tagline {
    position: absolute;
    top: 311px;
    width: 100%;
    text-align: center;
    color: var(--white);
    font-weight: 700;
    font-size: 22px;
  }
  .services {
    position: absolute;
    top: 425px;
    width: 100%;
    text-align: center;
    color: var(--ink-navy);
    font-weight: 300;
    font-size: 24px;
    line-height: 40px;
    list-style: none;
  }
</style>
</head>
<body>
<main class="canvas">

  <section class="card card--front" aria-label="Business card front">
    <div class="card__texture" role="img" aria-label="Faint repeating pattern of circled plus, minus, multiply and divide signs"></div>

    <div class="brand">
      <div class="brand__square"></div>
      <div class="brand__name">KESTREL BUSINESS<br>ACCOUNTANTS<br>PTY LTD</div>
    </div>
    <div class="band band--rule" style="top:168px"></div>

    <svg class="arrow arrow--up" viewBox="0 0 28 18" aria-hidden="true"><polygon points="14,0 28,18 0,18" fill="#ffffff"/></svg>
    <p class="role">CPA Director</p>
    <p class="person">MILES HARTLEY</p>
    <svg class="arrow arrow--down" viewBox="0 0 28 18" aria-hidden="true"><polygon points="0,0 28,0 14,18" fill="#ffffff"/></svg>

    <p class="contact contact--phone"><span class="contact__label">T :</span> 0413 8064 91</p>
    <div class="band band--strip" style="top:616px"></div>
    <p class="contact contact--email"><span class="contact__label">E :</span> kestrel@pallinet.com.au</p>
    <div class="band band--strip" style="top:697px"></div>
  </section>

  <section class="card card--back" aria-label="Business card back">
    <div class="card__texture" role="img" aria-label="Faint repeating pattern of circled plus, minus, multiply and divide signs"></div>
    <p class="tagline">"Kestrel Sight for your Business"</p>
    <div class="band band--rule" style="top:384px"></div>
    <ul class="services">
      <li>Business Consulting</li>
      <li>Taxation Superannuation</li>
    </ul>
  </section>

</main>
</body>
</html>
```